Harborline Coverage (02)

We're designing a website to sell Medicare Supplements. Attached is the content we want to say and general layout, but please use your best knowledge to make it better. This platform is intentionally simplistic because this is reaching an older demographic, so it should be very straightforward, attention-grabbing and extremely user-friendly, while still appearing reliable and professional.
This should be a two-page web design. The homepage has information on Medicare supplements (script in image attached below) along with a button to input zip code. This triggers a window to pop up asking for personal information (will also be listed in attachment).
This brings you to the second page that lists out the medicare supplement companies and plans based on inputed information. We just want to see the design you have in mind, so it doesn't matter what information you put in this section. Feel free to reference/replicate the information in image 3 in the doc. There should be a section where you can filter results by company, premium price, or coverage plans.
Target Market(s)
Seniors, 65+
Industry/Entity Type
Insurance
Number of Pages Required
2 page
Look and feel
Each slider illustrates characteristics of the customer's brand and the style your logo design should communicate.

```html
<!DOCTYPE html>
<html lang="en">
<head>
<meta charset="utf-8">
<title>Harborline Coverage – Home and Plans</title>
<link rel="stylesheet" href="https://fonts.googleapis.com/css2?family=Montserrat:wght@600;700&family=Roboto:wght@400;500;700&display=swap">
<style>
:root{
  --stage:#21a696;
  --teal:#1fa595;
  --teal-light:#cfe9e5;
  --hero:#17302f;
  --ink:#1f2a2a;
  --text:#3d4444;
  --muted:#7b8585;
  --line:#dfe3e3;
  --soft:#f4f4f4;
  --card-side:#f2f3f3;
  --footer:#eef2f6;
  --brand-purple:#6b2c85;
  --white:#ffffff;
}
*{box-sizing:border-box;margin:0;padding:0}
html,body{width:768px;height:1200px;overflow:hidden;background:var(--stage)}
body{font-family:Roboto,Arial,sans-serif;color:var(--text)}
.stage{position:absolute;left:0;top:0;width:1540px;height:2406px;transform:scale(.4987);transform-origin:0 0;background:var(--stage)}
.page{position:absolute;top:69px;width:670px;height:2252px;background:var(--soft);overflow:hidden}
.page--home{left:75px}
.page--quote{left:802px}
.abs{position:absolute}
/* header */
.site-header{left:0;top:0;width:670px;height:41px;background:var(--white)}
.brand{display:flex;align-items:center;gap:5px;font-family:Roboto,sans-serif;font-weight:700;font-size:11.5px;color:var(--teal)}
.brand-dot{width:13px;height:13px;border-radius:50%;background:var(--hero)}
.site-header .brand{position:absolute;left:97px;top:13px}
.nav{position:absolute;top:16px;font-size:9px;color:var(--ink)}
.nav-call{position:absolute;left:468px;top:16px;font-size:8.5px;color:var(--ink);display:flex;align-items:center;gap:3px}
.nav-call b{color:var(--teal);font-weight:700}
/* hero */
.hero{left:0;top:41px;width:670px;height:252px}
.hero-photo{left:0;top:0;width:300px;height:205px;background:linear-gradient(90deg,#3b4f4c 0%,#2a4240 55%,rgba(23,48,47,0) 100%);opacity:.85}
.hero-title{left:0;width:670px;text-align:center}
.hero h1{top:73px;font-family:Montserrat,sans-serif;font-weight:700;font-size:29px;color:var(--white)}
.hero .lead{top:114px;font-size:9px;color:var(--white)}
.hero .call{top:134px;font-size:17px;font-weight:500;color:var(--teal)}
.hero .cont{top:160px;font-size:11px;font-weight:500;color:var(--white)}
.zip{position:absolute;left:188px;top:192px;width:203px;height:28px;border-radius:14px;background:var(--white);font-size:10.5px;color:var(--muted);padding:7px 11px}
.zip-btn{position:absolute;left:396px;top:192px;width:86px;height:28px;border-radius:14px;background:var(--teal);color:var(--white);font-size:8px;font-weight:700;text-align:center;line-height:28px;letter-spacing:.3px}
/* info */
.info h2{font-family:Roboto,sans-serif;font-weight:500;font-size:14.5px;color:var(--ink);line-height:17px}
.para{font-size:7.3px;line-height:13px;color:var(--text)}
.ticks{list-style:none;font-size:7.3px;line-height:9px}
.ticks li{margin-bottom:6.5px;padding-left:5px;position:relative}
.ticks li::before{content:"•";position:absolute;left:0}
.ticks b{color:var(--teal);font-weight:500;font-size:9.5px}
.photo-circle{border-radius:50%}
.note{left:0;width:670px;text-align:center;font-size:10px;line-height:17px;color:var(--ink)}
/* plans */
.plans{left:0;top:919px;width:670px;height:1095px;background:var(--white);border-top:2px solid #e8eaea}
.plans h2{position:absolute;left:96px;top:22px;font-family:Montserrat,sans-serif;font-weight:600;font-size:16px;color:var(--ink)}
.sort{position:absolute;left:447px;top:28px;font-size:7px;color:var(--text)}
.select{position:absolute;height:17px;border-radius:9px;background:#eef0f0;font-size:5.5px;color:var(--muted);padding:5px 7px}
.select::after{content:"▾";position:absolute;right:7px;top:4px;font-size:6px}
.filter{position:absolute;left:96px;top:70px;width:110px;height:383px;border:1px solid var(--line);background:var(--white)}
.filter h3{font-size:8.5px;font-weight:700;color:var(--ink);padding:8px 8px 6px;border-bottom:1px solid var(--line)}
.filter-group{padding:6px 8px 7px;border-bottom:1px solid var(--line)}
.filter-group:last-child{border-bottom:none}
.filter-group h4{font-size:7px;font-weight:500;color:var(--teal);margin-bottom:5px}
.filter-group li{list-style:none;font-size:6.5px;line-height:13.8px;color:var(--text);display:flex;align-items:center;gap:4px}
.filter-group li::before{content:"";width:5px;height:5px;border:.7px solid #9aa2a2}
.card{position:absolute;left:226px;width:347px;height:178px;border:1px solid var(--line);border-radius:4px;background:var(--white);overflow:hidden}
.card-side{position:absolute;left:0;top:0;width:116px;height:154px;background:var(--card-side);text-align:center}
.card-price{padding-top:14px;font-size:11px;color:var(--ink)}
.card-term{font-size:11px;font-weight:500;color:var(--ink);margin-top:3px}
.enroll{display:block;margin:7px auto 0;width:76px;height:17px;border-radius:9px;background:var(--teal);color:var(--white);font-size:6px;font-weight:700;line-height:17px}
.fav{position:absolute;left:0;width:116px;top:95px;text-align:center;font-size:6.5px;color:var(--text)}
.fav svg{display:block;margin:0 auto 3px}
.card-body{position:absolute;left:130px;top:0;width:210px}
.carrier{position:absolute;left:0;top:9px;font-size:12px;font-weight:700;color:var(--brand-purple)}
.plan-name{position:absolute;left:0;top:28px;font-size:7.5px;font-weight:500;color:var(--ink)}
.stats{position:absolute;left:0;top:44px;width:202px;height:37px;display:flex}
.stat{width:77px;text-align:center}
.stat b{display:block;font-size:10.5px;font-weight:500;color:var(--ink)}
.stat span{font-size:5px;color:var(--muted)}
.stat--drugs{width:60px;border-left:1px solid var(--line);padding-top:2px}
.chip{display:inline-block;border:.7px solid var(--line);color:var(--teal);font-size:5px;padding:1.5px 3px}
.stat--drugs span{display:block;margin-top:3px}
.row-label{position:absolute;left:0;font-size:6px;font-weight:700;color:var(--ink)}
.features{position:absolute;left:60px;top:112px;width:140px;display:grid;grid-template-columns:68px 68px;font-size:5.5px;line-height:10.5px;color:var(--text)}
.features span::before{content:"✓ ";color:var(--teal)}
.card-foot{position:absolute;left:0;top:154px;width:347px;height:24px;border-top:1px solid var(--line)}
.more{position:absolute;left:10px;top:8px;font-size:6px;font-weight:500;color:var(--teal)}
.compare{position:absolute;right:6px;top:4px;width:56px;height:16px;border-radius:8px;background:#eef0f0;font-size:6px;color:var(--teal);text-align:center;line-height:16px}
/* footer */
.site-footer{left:0;top:2014px;width:670px;height:238px;background:var(--footer)}
.site-footer .brand{position:absolute;left:270px;top:34px}
.foot-rule{position:absolute;left:96px;top:64px;width:477px;height:1px;background:#d7dde3}
.foot-col{position:absolute;top:84px;font-size:6px;line-height:10.9px;color:var(--text)}
.foot-col h5{font-size:9px;font-weight:500;color:var(--ink);margin-bottom:8px}
.contact-row{display:flex;gap:6px;margin-bottom:9px}
.copy{position:absolute;left:96px;top:213px;font-size:6.5px;color:var(--ink)}
.socials{position:absolute;left:508px;top:208px;display:flex;gap:3px}
.socials span{width:13px;height:13px;border-radius:50%;background:var(--teal)}
/* dim + modal */
.dim{position:absolute;left:0;top:0;width:670px;height:2252px;background:rgba(30,30,30,.62)}
.modal{position:absolute;left:939px;top:963px;width:393px;height:549px;background:var(--white);border-radius:8px}
.modal h2{position:absolute;left:40px;top:22px;font-family:Montserrat,sans-serif;font-weight:600;font-size:19px;color:var(--ink)}
.modal .para{position:absolute;left:40px;top:52px;width:305px;font-size:6.8px;line-height:13px}
.mlabel{position:absolute;font-size:8px;font-weight:500;color:var(--ink)}
.mlabel i{color:#e0383e;font-style:normal}
.mfield{position:absolute;height:20px;border:1px solid var(--line);border-radius:10px;background:#f7f8f8;font-size:5.5px;color:var(--muted);padding:6px 8px}
.msel::after{content:"▾";position:absolute;right:8px;top:5px}
.radio{position:absolute;left:40px;top:165px;font-size:6px;color:var(--text);display:flex;gap:8px}
.radio span::before{content:"○ "}
.mbtn{position:absolute;left:40px;top:470px;width:95px;height:22px;border-radius:11px;background:var(--teal);color:var(--white);font-size:7px;font-weight:700;text-align:center;line-height:22px}
.mcancel{position:absolute;left:147px;top:475px;font-size:7.5px;color:var(--teal);text-decoration:underline}
.mclose{position:absolute;left:1305px;top:957px;width:30px;height:30px;border-radius:50%;background:var(--teal);border:2px solid var(--white);color:var(--white);font-family:Montserrat,sans-serif;font-weight:700;font-size:15px;text-align:center;line-height:26px}
</style>
</head>
<body>
<div class="stage">

<!-- ============ HOME PAGE ============ -->
<div class="page page--home">
  <header class="site-header abs">
    <div class="brand"><span class="brand-dot"></span>Harborline Coverage</div>
    <span class="nav" style="left:261px">Medicare ▾</span>
    <span class="nav" style="left:326px">Get Quotes</span>
    <span class="nav" style="left:402px">Blog</span>
    <span class="nav-call"><svg width="9" height="9" viewBox="0 0 24 24"><path fill="#1f2a2a" d="M6.6 10.8a15 15 0 0 0 6.6 6.6l2.2-2.2a1 1 0 0 1 1-.25 11 11 0 0 0 3.6.6 1 1 0 0 1 1 1V20a1 1 0 0 1-1 1A17 17 0 0 1 3 4a1 1 0 0 1 1-1h3.5a1 1 0 0 1 1 1c0 1.25.2 2.45.6 3.6a1 1 0 0 1-.25 1z"/></svg>Call :<b>(800) 555-0142</b></span>
  </header>
  <section class="hero abs">
    <svg class="abs" style="left:0;top:0" width="670" height="252" viewBox="0 0 670 252">
      <path d="M0 0H670V196C520 215 300 222 0 232Z" fill="#17302f"/>
      <path d="M0 214C250 228 470 212 670 196V212C470 230 250 245 0 250Z" fill="#cfe9e5"/>
    </svg>
    <div class="hero-photo abs" role="img" aria-label="Smiling senior couple photograph"></div>
    <h1 class="hero-title abs">Harborline Coverage</h1>
    <p class="hero-title lead abs">Be confident choosing the Medicare Supplement plan that's right for you.</p>
    <p class="hero-title call abs">Call (800) 555-0142 for more information,</p>
    <p class="hero-title cont abs">or continue to view our premium plans below:</p>
    <div class="zip">Enter Zip Code</div>
    <div class="zip-btn">FIND PLANS</div>
  </section>
  <section class="info">
    <h2 class="abs" style="left:96px;top:324px">What is a Medicare Supplement plan?</h2>
    <p class="para abs" style="left:97px;top:354px;width:285px">Each Medicare Supplement insurance plan offers a different level of basic benefits, but each lettered plan will include the same standardized basic benefits regardless of insurance company and location. Medicare Supplement insurance plans do not always cover vision, dental, long-term care, or hearing aids, but all plans must cover at least a portion of the following basic benefits:</p>
    <ul class="ticks abs" style="left:108px;top:434px;width:275px">
      <li>Medicare Part A coinsurance costs up to an additional 365 days after Medicare benefits are exhausted</li>
      <li>Medicare Part A hospice care coinsurance or copayments</li>
      <li>Medicare Part B coinsurance or copayments</li>
      <li>First three pints of blood used in a medical procedure</li>
    </ul>
    <div class="photo-circle abs" style="left:393px;top:316px;width:204px;height:204px;background:radial-gradient(circle at 55% 55%,#3e4d7a 0%,#6e7aa0 35%,#c9cbd2 70%,#e6e6e8 100%)" role="img" aria-label="Blueberries and supplement capsules"></div>
    <div class="photo-circle abs" style="left:63px;top:557px;width:204px;height:204px;background:radial-gradient(circle at 50% 55%,#e8c0c0 0%,#d9a3a2 40%,#9a7a72 80%,#6f5850 100%)" role="img" aria-label="Hands holding a pink piggy bank"></div>
    <h2 class="abs" style="left:300px;top:571px;width:260px">Medicare Supplement insurance plan costs</h2>
    <p class="para abs" style="left:301px;top:612px;width:285px">Although private insurance companies are required to offer the same basic benefits for each lettered plan, they do have the ability to charge different premiums. You might want to shop around to find a Medicare Supplement insurance plan that may fit your medical and financial needs. Insurance companies may price their plan premiums in any of the following ways:</p>
    <ul class="ticks abs" style="left:312px;top:688px;width:272px">
      <li style="margin-bottom:14px"><b>Community no-age-rated:</b> These Medicare Supplement insurance plans charge premiums that are the same across the board, regardless of age.</li>
      <li style="margin-bottom:14px"><b>Issue-age-rated:</b> These plans base their premiums on your age when you first enrolled in the policy. Therefore, the younger you are when you enroll in this type of plan, the lower your premium will be.</li>
      <li><b>Attained-age-rated:</b> Like issue-age-rated, these plans base their premiums on the age you were when you first bought a policy, but unlike issue-age-rated, premiums increase as you get older.</li>
    </ul>
    <p class="note abs" style="top:851px">Please note that no matter what rating method an insurance company uses,<br>premiums may increase over time for reasons other than age, such as inflation.</p>
  </section>
  <section class="plans abs">
    <h2>Medicare Advantage Plans</h2>
    <span class="sort">Sort by</span>
    <div class="select" style="left:480px;top:24px;width:93px">Low Price</div>
    <aside class="filter">
      <h3>Filter Plans by</h3>
      <div class="filter-group"><h4>▾ Company</h4><ul><li>At vero eos et asamus</li><li>Tusto odio dignissmos</li><li>Ducimusui blanditiis</li><li>Praesentium volptatum</li><li>Deleniti atque corrupt</li><li>Quos dolores</li></ul></div>
      <div class="filter-group"><h4>▾ Premium Price</h4><ul><li>No premium (6)</li><li>Under $50 (7)</li><li>$50 to $100 (1)</li><li>$100 to $200 (1)</li><li>$200 &amp; $300 (0)</li><li>$200 &amp; $300 (3)</li></ul></div>
      <div class="filter-group"><h4>▾ Plan Type</h4><ul><li>Sro eos et as</li><li>Tusto osmos</li><li>Ducimu blditiis</li><li>Praesem volptatum</li><li>Delenitue</li><li>Quos dolor</li></ul></div>
    </aside>
    <article class="card" style="top:70px"><div class="card-side"><p class="card-price">$50.00</p><p class="card-term">Monthly Premium</p><span class="enroll">ENROLL NOW</span></div><div class="fav"><svg width="13" height="12" viewBox="0 0 24 22"><path d="M12 20S2 13.5 2 7.5A5 5 0 0 1 12 5a5 5 0 0 1 10 2.5C22 13.5 12 20 12 20z" fill="none" stroke="#e0383e" stroke-width="2"/></svg>Add to Favorites</div><div class="card-body"><span class="carrier">Northvale</span><span class="plan-name">Neueporrouisuam est ui dolorem</span><div class="stats"><div class="stat"><b>$0</b><span>Neue orro uisqam</span></div><div class="stat"><b>$40</b><span>Neue orro uisqam</span></div><div class="stat stat--drugs"><span class="chip">+ Add Drugs</span><span>Drugs Covered</span></div></div><span class="row-label" style="top:96px">Doctor Coverage:</span><span class="chip abs" style="left:66px;top:95px">+ Add your doctors to see coverage</span><span class="row-label" style="top:112px">Plan Features:</span><div class="features"><span>Rx Drugs</span><span>Vision</span><span>Hospital &amp; Medical</span><span>Hearing</span><span>Dental</span><span>Fitness Benefits</span></div></div><div class="card-foot"><span class="more">View More Details ▾</span><span class="compare">☐ Compare</span></div></article>
    <article class="card" style="top:268px"><div class="card-side"><p class="card-price">$50.00</p><p class="card-term">Monthly Premium</p><span class="enroll">ENROLL NOW</span></div><div class="fav"><svg width="13" height="12" viewBox="0 0 24 22"><path d="M12 20S2 13.5 2 7.5A5 5 0 0 1 12 5a5 5 0 0 1 10 2.5C22 13.5 12 20 12 20z" fill="none" stroke="#e0383e" stroke-width="2"/></svg>Add to Favorites</div><div class="card-body"><span class="carrier">Northvale</span><span class="plan-name">Neueporrouisuam est ui dolorem</span><div class="stats"><div class="stat"><b>$0</b><span>Neue orro uisqam</span></div><div class="stat"><b>$40</b><span>Neue orro uisqam</span></div><div class="stat stat--drugs"><span class="chip">+ Add Drugs</span><span>Drugs Covered</span></div></div><span class="row-label" style="top:96px">Doctor Coverage:</span><span class="chip abs" style="left:66px;top:95px">+ Add your doctors to see coverage</span><span class="row-label" style="top:112px">Plan Features:</span><div class="features"><span>Rx Drugs</span><span>Vision</span><span>Hospital &amp; Medical</span><span>Hearing</span><span>Dental</span><span>Fitness Benefits</span></div></div><div class="card-foot"><span class="more">View More Details ▾</span><span class="compare">☐ Compare</span></div></article>
    <article class="card" style="top:466px"><div class="card-side"><p class="card-price">$50.00</p><p class="card-term">Monthly Premium</p><span class="enroll">ENROLL NOW</span></div><div class="fav"><svg width="13" height="12" viewBox="0 0 24 22"><path d="M12 20S2 13.5 2 7.5A5 5 0 0 1 12 5a5 5 0 0 1 10 2.5C22 13.5 12 20 12 20z" fill="none" stroke="#e0383e" stroke-width="2"/></svg>Add to Favorites</div><div class="card-body"><span class="carrier">Northvale</span><span class="plan-name">Neueporrouisuam est ui dolorem</span><div class="stats"><div class="stat"><b>$0</b><span>Neue orro uisqam</span></div><div class="stat"><b>$40</b><span>Neue orro uisqam</span></div><div class="stat stat--drugs"><span class="chip">+ Add Drugs</span><span>Drugs Covered</span></div></div><span class="row-label" style="top:96px">Doctor Coverage:</span><span class="chip abs" style="left:66px;top:95px">+ Add your doctors to see coverage</span><span class="row-label" style="top:112px">Plan Features:</span><div class="features"><span>Rx Drugs</span><span>Vision</span><span>Hospital &amp; Medical</span><span>Hearing</span><span>Dental</span><span>Fitness Benefits</span></div></div><div class="card-foot"><span class="more">View More Details ▾</span><span class="compare">☐ Compare</span></div></article>
    <article class="card" style="top:664px"><div class="card-side"><p class="card-price">$50.00</p><p class="card-term">Monthly Premium</p><span class="enroll">ENROLL NOW</span></div><div class="fav"><svg width="13" height="12" viewBox="0 0 24 22"><path d="M12 20S2 13.5 2 7.5A5 5 0 0 1 12 5a5 5 0 0 1 10 2.5C22 13.5 12 20 12 20z" fill="none" stroke="#e0383e" stroke-width="2"/></svg>Add to Favorites</div><div class="card-body"><span class="carrier">Northvale</span><span class="plan-name">Neueporrouisuam est ui dolorem</span><div class="stats"><div class="stat"><b>$0</b><span>Neue orro uisqam</span></div><div class="stat"><b>$40</b><span>Neue orro uisqam</span></div><div class="stat stat--drugs"><span class="chip">+ Add Drugs</span><span>Drugs Covered</span></div></div><span class="row-label" style="top:96px">Doctor Coverage:</span><span class="chip abs" style="left:66px;top:95px">+ Add your doctors to see coverage</span><span class="row-label" style="top:112px">Plan Features:</span><div class="features"><span>Rx Drugs</span><span>Vision</span><span>Hospital &amp; Medical</span><span>Hearing</span><span>Dental</span><span>Fitness Benefits</span></div></div><div class="card-foot"><span class="more">View More Details ▾</span><span class="compare">☐ Compare</span></div></article>
    <article class="card" style="top:862px"><div class="card-side"><p class="card-price">$50.00</p><p class="card-term">Monthly Premium</p><span class="enroll">ENROLL NOW</span></div><div class="fav"><svg width="13" height="12" viewBox="0 0 24 22"><path d="M12 20S2 13.5 2 7.5A5 5 0 0 1 12 5a5 5 0 0 1 10 2.5C22 13.5 12 20 12 20z" fill="none" stroke="#e0383e" stroke-width="2"/></svg>Add to Favorites</div><div class="card-body"><span class="carrier">Northvale</span><span class="plan-name">Neueporrouisuam est ui dolorem</span><div class="stats"><div class="stat"><b>$0</b><span>Neue orro uisqam</span></div><div class="stat"><b>$40</b><span>Neue orro uisqam</span></div><div class="stat stat--drugs"><span class="chip">+ Add Drugs</span><span>Drugs Covered</span></div></div><span class="row-label" style="top:96px">Doctor Coverage:</span><span class="chip abs" style="left:66px;top:95px">+ Add your doctors to see coverage</span><span class="row-label" style="top:112px">Plan Features:</span><div class="features"><span>Rx Drugs</span><span>Vision</span><span>Hospital &amp; Medical</span><span>Hearing</span><span>Dental</span><span>Fitness Benefits</span></div></div><div class="card-foot"><span class="more">View More Details ▾</span><span class="compare">☐ Compare</span></div></article>
  </section>
  <footer class="site-footer abs">
    <div class="brand"><span class="brand-dot"></span>Harborline Coverage</div>
    <div class="foot-rule"></div>
    <div class="foot-col" style="left:96px;width:130px"><h5>Contact</h5>
      <div class="contact-row"><svg width="10" height="12" viewBox="0 0 20 24"><path d="M10 1a8 8 0 0 0-8 8c0 6 8 14 8 14s8-8 8-14a8 8 0 0 0-8-8zm0 11a3 3 0 1 1 0-6 3 3 0 0 1 0 6z" fill="none" stroke="#1fa595" stroke-width="1.6"/></svg><span>412 Maple Row,<br>Eastbrook, Ohio</span></div>
      <div class="contact-row"><svg width="11" height="11" viewBox="0 0 24 24"><path fill="none" stroke="#1fa595" stroke-width="1.6" d="M6.6 10.8a15 15 0 0 0 6.6 6.6l2.2-2.2a1 1 0 0 1 1-.25 11 11 0 0 0 3.6.6 1 1 0 0 1 1 1V20a1 1 0 0 1-1 1A17 17 0 0 1 3 4a1 1 0 0 1 1-1h3.5a1 1 0 0 1 1 1c0 1.25.2 2.45.6 3.6a1 1 0 0 1-.25 1z"/></svg><span>1 800 555 013 27<br>1 800 555 019 64</span></div>
      <div class="contact-row"><svg width="12" height="10" viewBox="0 0 24 18"><rect x="1" y="1" width="22" height="16" fill="none" stroke="#1fa595" stroke-width="1.6"/><path d="M1 1l11 9 11-9" fill="none" stroke="#1fa595" stroke-width="1.6"/></svg><span>hello@harborline.test<br>team@harborline.test</span></div>
    </div>
    <div class="foot-col" style="left:246px"><h5>Company</h5>Lorem ipsum dolo<br>Consectetur adipiscing elit.<br>Fusce eget leo tincid<br>Donec consequat<br>Praesent elementum<br>Jmauris posueret</div>
    <div class="foot-col" style="left:366px"><h5>Information</h5>Lorem ipsum dolo<br>Consectetur adipiscing elit.<br>Fusce eget leo tincid<br>Donec consequat<br>Praesent elementum<br>Jmauris posuer</div>
    <div class="foot-col" style="left:494px"><h5>Other Links</h5>Lorem ipsum dolo<br>Consectetur adipiscing elit.<br>Fusce eget leo tincid<br>Donec consequat<br>Praesent elementum<br>Jmauris posueret</div>
    <p class="copy">Copyright © 2020 Harborline Coverage. All Rights Reserved</p>
    <div class="socials"><span></span><span></span><span></span><span></span></div>
  </footer>
</div>

<!-- ============ QUOTE STATE ============ -->
<div class="page page--quote">
  <header class="site-header abs">
    <div class="brand"><span class="brand-dot"></span>Harborline Coverage</div>
    <span class="nav" style="left:261px">Medicare ▾</span>
    <span class="nav" style="left:326px">Get Quotes</span>
    <span class="nav" style="left:402px">Blog</span>
    <span class="nav-call"><svg width="9" height="9" viewBox="0 0 24 24"><path fill="#1f2a2a" d="M6.6 10.8a15 15 0 0 0 6.6 6.6l2.2-2.2a1 1 0 0 1 1-.25 11 11 0 0 0 3.6.6 1 1 0 0 1 1 1V20a1 1 0 0 1-1 1A17 17 0 0 1 3 4a1 1 0 0 1 1-1h3.5a1 1 0 0 1 1 1c0 1.25.2 2.45.6 3.6a1 1 0 0 1-.25 1z"/></svg>Call :<b>(800) 555-0142</b></span>
  </header>
  <section class="hero abs">
    <svg class="abs" style="left:0;top:0" width="670" height="252" viewBox="0 0 670 252">
      <path d="M0 0H670V196C520 215 300 222 0 232Z" fill="#17302f"/>
      <path d="M0 214C250 228 470 212 670 196V212C470 230 250 245 0 250Z" fill="#cfe9e5"/>
    </svg>
    <div class="hero-photo abs" role="img" aria-label="Smiling senior couple photograph"></div>
    <h1 class="hero-title abs">Harborline Coverage</h1>
    <p class="hero-title lead abs">Be confident choosing the Medicare Supplement plan that's right for you.</p>
    <p class="hero-title call abs">Call (800) 555-0142 for more information,</p>
    <p class="hero-title cont abs">or continue to view our premium plans below:</p>
    <div class="zip">Enter Zip Code</div>
    <div class="zip-btn">FIND PLANS</div>
  </section>
  <section class="info">
    <h2 class="abs" style="left:96px;top:324px">What is a Medicare Supplement plan?</h2>
    <p class="para abs" style="left:97px;top:354px;width:285px">Each Medicare Supplement insurance plan offers a different level of basic benefits, but each lettered plan will include the same standardized basic benefits regardless of insurance company and location. Medicare Supplement insurance plans do not always cover vision, dental, long-term care, or hearing aids, but all plans must cover at least a portion of the following basic benefits:</p>
    <ul class="ticks abs" style="left:108px;top:434px;width:275px">
      <li>Medicare Part A coinsurance costs up to an additional 365 days after Medicare benefits are exhausted</li>
      <li>Medicare Part A hospice care coinsurance or copayments</li>
      <li>Medicare Part B coinsurance or copayments</li>
      <li>First three pints of blood used in a medical procedure</li>
    </ul>
    <div class="photo-circle abs" style="left:393px;top:316px;width:204px;height:204px;background:radial-gradient(circle at 55% 55%,#3e4d7a 0%,#6e7aa0 35%,#c9cbd2 70%,#e6e6e8 100%)" role="img" aria-label="Blueberries and supplement capsules"></div>
    <div class="photo-circle abs" style="left:63px;top:557px;width:204px;height:204px;background:radial-gradient(circle at 50% 55%,#e8c0c0 0%,#d9a3a2 40%,#9a7a72 80%,#6f5850 100%)" role="img" aria-label="Hands holding a pink piggy bank"></div>
    <h2 class="abs" style="left:300px;top:571px;width:260px">Medicare Supplement insurance plan costs</h2>
    <p class="para abs" style="left:301px;top:612px;width:285px">Although private insurance companies are required to offer the same basic benefits for each lettered plan, they do have the ability to charge different premiums. You might want to shop around to find a Medicare Supplement insurance plan that may fit your medical and financial needs. Insurance companies may price their plan premiums in any of the following ways:</p>
    <ul class="ticks abs" style="left:312px;top:688px;width:272px">
      <li style="margin-bottom:14px"><b>Community no-age-rated:</b> These Medicare Supplement insurance plans charge premiums that are the same across the board, regardless of age.</li>
      <li style="margin-bottom:14px"><b>Issue-age-rated:</b> These plans base their premiums on your age when you first enrolled in the policy. Therefore, the younger you are when you enroll in this type of plan, the lower your premium will be.</li>
      <li><b>Attained-age-rated:</b> Like issue-age-rated, these plans base their premiums on the age you were when you first bought a policy, but unlike issue-age-rated, premiums increase as you get older.</li>
    </ul>
    <p class="note abs" style="top:851px">Please note that no matter what rating method an insurance company uses,<br>premiums may increase over time for reasons other than age, such as inflation.</p>
  </section>
  <section class="plans abs">
    <h2>Medicare Advantage Plans</h2>
    <span class="sort">Sort by</span>
    <div class="select" style="left:480px;top:24px;width:93px">Low Price</div>
    <aside class="filter">
      <h3>Filter Plans by</h3>
      <div class="filter-group"><h4>▾ Company</h4><ul><li>At vero eos et asamus</li><li>Tusto odio dignissmos</li><li>Ducimusui blanditiis</li><li>Praesentium volptatum</li><li>Deleniti atque corrupt</li><li>Quos dolores</li></ul></div>
      <div class="filter-group"><h4>▾ Premium Price</h4><ul><li>No premium (6)</li><li>Under $50 (7)</li><li>$50 to $100 (1)</li><li>$100 to $200 (1)</li><li>$200 &amp; $300 (0)</li><li>$200 &amp; $300 (3)</li></ul></div>
      <div class="filter-group"><h4>▾ Plan Type</h4><ul><li>Sro eos et as</li><li>Tusto osmos</li><li>Ducimu blditiis</li><li>Praesem volptatum</li><li>Delenitue</li><li>Quos dolor</li></ul></div>
    </aside>
    <article class="card" style="top:70px"><div class="card-side"><p class="card-price">$50.00</p><p class="card-term">Monthly Premium</p><span class="enroll">ENROLL NOW</span></div><div class="fav"><svg width="13" height="12" viewBox="0 0 24 22"><path d="M12 20S2 13.5 2 7.5A5 5 0 0 1 12 5a5 5 0 0 1 10 2.5C22 13.5 12 20 12 20z" fill="none" stroke="#e0383e" stroke-width="2"/></svg>Add to Favorites</div><div class="card-body"><span class="carrier">Northvale</span><span class="plan-name">Neueporrouisuam est ui dolorem</span><div class="stats"><div class="stat"><b>$0</b><span>Neue orro uisqam</span></div><div class="stat"><b>$40</b><span>Neue orro uisqam</span></div><div class="stat stat--drugs"><span class="chip">+ Add Drugs</span><span>Drugs Covered</span></div></div><span class="row-label" style="top:96px">Doctor Coverage:</span><span class="chip abs" style="left:66px;top:95px">+ Add your doctors to see coverage</span><span class="row-label" style="top:112px">Plan Features:</span><div class="features"><span>Rx Drugs</span><span>Vision</span><span>Hospital &amp; Medical</span><span>Hearing</span><span>Dental</span><span>Fitness Benefits</span></div></div><div class="card-foot"><span class="more">View More Details ▾</span><span class="compare">☐ Compare</span></div></article>
    <article class="card" style="top:268px"><div class="card-side"><p class="card-price">$50.00</p><p class="card-term">Monthly Premium</p><span class="enroll">ENROLL NOW</span></div><div class="fav"><svg width="13" height="12" viewBox="0 0 24 22"><path d="M12 20S2 13.5 2 7.5A5 5 0 0 1 12 5a5 5 0 0 1 10 2.5C22 13.5 12 20 12 20z" fill="none" stroke="#e0383e" stroke-width="2"/></svg>Add to Favorites</div><div class="card-body"><span class="carrier">Northvale</span><span class="plan-name">Neueporrouisuam est ui dolorem</span><div class="stats"><div class="stat"><b>$0</b><span>Neue orro uisqam</span></div><div class="stat"><b>$40</b><span>Neue orro uisqam</span></div><div class="stat stat--drugs"><span class="chip">+ Add Drugs</span><span>Drugs Covered</span></div></div><span class="row-label" style="top:96px">Doctor Coverage:</span><span class="chip abs" style="left:66px;top:95px">+ Add your doctors to see coverage</span><span class="row-label" style="top:112px">Plan Features:</span><div class="features"><span>Rx Drugs</span><span>Vision</span><span>Hospital &amp; Medical</span><span>Hearing</span><span>Dental</span><span>Fitness Benefits</span></div></div><div class="card-foot"><span class="more">View More Details ▾</span><span class="compare">☐ Compare</span></div></article>
    <article class="card" style="top:466px"><div class="card-side"><p class="card-price">$50.00</p><p class="card-term">Monthly Premium</p><span class="enroll">ENROLL NOW</span></div><div class="fav"><svg width="13" height="12" viewBox="0 0 24 22"><path d="M12 20S2 13.5 2 7.5A5 5 0 0 1 12 5a5 5 0 0 1 10 2.5C22 13.5 12 20 12 20z" fill="none" stroke="#e0383e" stroke-width="2"/></svg>Add to Favorites</div><div class="card-body"><span class="carrier">Northvale</span><span class="plan-name">Neueporrouisuam est ui dolorem</span><div class="stats"><div class="stat"><b>$0</b><span>Neue orro uisqam</span></div><div class="stat"><b>$40</b><span>Neue orro uisqam</span></div><div class="stat stat--drugs"><span class="chip">+ Add Drugs</span><span>Drugs Covered</span></div></div><span class="row-label" style="top:96px">Doctor Coverage:</span><span class="chip abs" style="left:66px;top:95px">+ Add your doctors to see coverage</span><span class="row-label" style="top:112px">Plan Features:</span><div class="features"><span>Rx Drugs</span><span>Vision</span><span>Hospital &amp; Medical</span><span>Hearing</span><span>Dental</span><span>Fitness Benefits</span></div></div><div class="card-foot"><span class="more">View More Details ▾</span><span class="compare">☐ Compare</span></div></article>
    <article class="card" style="top:664px"><div class="card-side"><p class="card-price">$50.00</p><p class="card-term">Monthly Premium</p><span class="enroll">ENROLL NOW</span></div><div class="fav"><svg width="13" height="12" viewBox="0 0 24 22"><path d="M12 20S2 13.5 2 7.5A5 5 0 0 1 12 5a5 5 0 0 1 10 2.5C22 13.5 12 20 12 20z" fill="none" stroke="#e0383e" stroke-width="2"/></svg>Add to Favorites</div><div class="card-body"><span class="carrier">Northvale</span><span class="plan-name">Neueporrouisuam est ui dolorem</span><div class="stats"><div class="stat"><b>$0</b><span>Neue orro uisqam</span></div><div class="stat"><b>$40</b><span>Neue orro uisqam</span></div><div class="stat stat--drugs"><span class="chip">+ Add Drugs</span><span>Drugs Covered</span></div></div><span class="row-label" style="top:96px">Doctor Coverage:</span><span class="chip abs" style="left:66px;top:95px">+ Add your doctors to see coverage</span><span class="row-label" style="top:112px">Plan Features:</span><div class="features"><span>Rx Drugs</span><span>Vision</span><span>Hospital &amp; Medical</span><span>Hearing</span><span>Dental</span><span>Fitness Benefits</span></div></div><div class="card-foot"><span class="more">View More Details ▾</span><span class="compare">☐ Compare</span></div></article>
    <article class="card" style="top:862px"><div class="card-side"><p class="card-price">$50.00</p><p class="card-term">Monthly Premium</p><span class="enroll">ENROLL NOW</span></div><div class="fav"><svg width="13" height="12" viewBox="0 0 24 22"><path d="M12 20S2 13.5 2 7.5A5 5 0 0 1 12 5a5 5 0 0 1 10 2.5C22 13.5 12 20 12 20z" fill="none" stroke="#e0383e" stroke-width="2"/></svg>Add to Favorites</div><div class="card-body"><span class="carrier">Northvale</span><span class="plan-name">Neueporrouisuam est ui dolorem</span><div class="stats"><div class="stat"><b>$0</b><span>Neue orro uisqam</span></div><div class="stat"><b>$40</b><span>Neue orro uisqam</span></div><div class="stat stat--drugs"><span class="chip">+ Add Drugs</span><span>Drugs Covered</span></div></div><span class="row-label" style="top:96px">Doctor Coverage:</span><span class="chip abs" style="left:66px;top:95px">+ Add your doctors to see coverage</span><span class="row-label" style="top:112px">Plan Features:</span><div class="features"><span>Rx Drugs</span><span>Vision</span><span>Hospital &amp; Medical</span><span>Hearing</span><span>Dental</span><span>Fitness Benefits</span></div></div><div class="card-foot"><span class="more">View More Details ▾</span><span class="compare">☐ Compare</span></div></article>
  </section>
  <footer class="site-footer abs">
    <div class="brand"><span class="brand-dot"></span>Harborline Coverage</div>
    <div class="foot-rule"></div>
    <div class="foot-col" style="left:96px;width:130px"><h5>Contact</h5>
      <div class="contact-row"><svg width="10" height="12" viewBox="0 0 20 24"><path d="M10 1a8 8 0 0 0-8 8c0 6 8 14 8 14s8-8 8-14a8 8 0 0 0-8-8zm0 11a3 3 0 1 1 0-6 3 3 0 0 1 0 6z" fill="none" stroke="#1fa595" stroke-width="1.6"/></svg><span>412 Maple Row,<br>Eastbrook, Ohio</span></div>
      <div class="contact-row"><svg width="11" height="11" viewBox="0 0 24 24"><path fill="none" stroke="#1fa595" stroke-width="1.6" d="M6.6 10.8a15 15 0 0 0 6.6 6.6l2.2-2.2a1 1 0 0 1 1-.25 11 11 0 0 0 3.6.6 1 1 0 0 1 1 1V20a1 1 0 0 1-1 1A17 17 0 0 1 3 4a1 1 0 0 1 1-1h3.5a1 1 0 0 1 1 1c0 1.25.2 2.45.6 3.6a1 1 0 0 1-.25 1z"/></svg><span>1 800 555 013 27<br>1 800 555 019 64</span></div>
      <div class="contact-row"><svg width="12" height="10" viewBox="0 0 24 18"><rect x="1" y="1" width="22" height="16" fill="none" stroke="#1fa595" stroke-width="1.6"/><path d="M1 1l11 9 11-9" fill="none" stroke="#1fa595" stroke-width="1.6"/></svg><span>hello@harborline.test<br>team@harborline.test</span></div>
    </div>
    <div class="foot-col" style="left:246px"><h5>Company</h5>Lorem ipsum dolo<br>Consectetur adipiscing elit.<br>Fusce eget leo tincid<br>Donec consequat<br>Praesent elementum<br>Jmauris posueret</div>
    <div class="foot-col" style="left:366px"><h5>Information</h5>Lorem ipsum dolo<br>Consectetur adipiscing elit.<br>Fusce eget leo tincid<br>Donec consequat<br>Praesent elementum<br>Jmauris posuer</div>
    <div class="foot-col" style="left:494px"><h5>Other Links</h5>Lorem ipsum dolo<br>Consectetur adipiscing elit.<br>Fusce eget leo tincid<br>Donec consequat<br>Praesent elementum<br>Jmauris posueret</div>
    <p class="copy">Copyright © 2020 Harborline Coverage. All Rights Reserved</p>
    <div class="socials"><span></span><span></span><span></span><span></span></div>
  </footer>
  <div class="dim"></div>
</div>

<!-- quote modal -->
<div class="modal" role="dialog" aria-label="Get A Quote">
  <h2>Get A Quote</h2>
  <p class="para">Sed ut perspiciatis unde omnis iste natus error sit voluptatem accusantium doloremque la udantium, totam rem aperiam, eaque ipsa quae ab illo invetore veritatis et quasi architecto beatae vitae dicta sunt explicabo.emo enim ipsam voluptatem quia voluptas sit aspernatu r autae dicta sunt explicaboemo enim ipsam voluptate</p>
  <span class="mlabel" style="left:40px;top:121px">Required <i>*</i></span>
  <span class="mlabel" style="left:40px;top:150px">Gender <i>*</i></span>
  <div class="radio"><span>Male</span><span>Female</span></div>
  <span class="mlabel" style="left:40px;top:180px">Age <i>*</i></span>
  <div class="mfield" style="left:40px;top:196px;width:153px"></div>
  <span class="mlabel" style="left:40px;top:224px">Date of Birth <i>*</i></span>
  <div class="mfield" style="left:40px;top:240px;width:153px">dd/mm/yyyy<span style="position:absolute;right:8px">▦</span></div>
  <span class="mlabel" style="left:40px;top:275px">Hospital Insurance (Part A)</span>
  <span class="mlabel" style="left:40px;top:292px;font-size:7px">Part A Month <i>*</i></span>
  <span class="mlabel" style="left:199px;top:292px;font-size:7px">Part A Year <i>*</i></span>
  <div class="mfield msel" style="left:40px;top:308px;width:153px">Month</div>
  <div class="mfield msel" style="left:199px;top:308px;width:153px">Year</div>
  <span class="mlabel" style="left:40px;top:342px">Medical Insurance (Part B)</span>
  <span class="mlabel" style="left:40px;top:359px;font-size:7px">Part B Month <i>*</i></span>
  <span class="mlabel" style="left:199px;top:359px;font-size:7px">Part B Year <i>*</i></span>
  <div class="mfield msel" style="left:40px;top:375px;width:153px">Month</div>
  <div class="mfield msel" style="left:199px;top:375px;width:153px">Year</div>
  <span class="mlabel" style="left:40px;top:418px">Desired Coverage Start Date <i>*</i></span>
  <div class="mfield" style="left:40px;top:434px;width:153px">▦</div>
  <span class="mbtn">COMPARE RATES</span>
  <span class="mcancel">Cancel</span>
</div>
<div class="mclose">X</div>

</div>
</body>
</html>
```